lawn sign

Lawn Sign
Roofing Gutters Windows

Target Market(s)

roofing

Font styles to use
Sans Serif

Colors
86cfc6
33a6d7
fbee3f
faa54b

Requirements
Must have
• my logo
Nice to have
• designer for now

```html
<!DOCTYPE html>
<html lang="en">
<head>
<meta charset="utf-8">
<title>Harlow Restoration Lawn Sign</title>
<link href="https://fonts.googleapis.com/css2?family=Cinzel:wght@400;700;900&display=swap" rel="stylesheet">
<style>
  :root {
    --canvas: #eef0f1;
    --sign: #ffffff;
    --teal: #14857f;
    --ink: #222222;
    --green: #8cc63f;
    --green-deep: #3aa14a;
    --ring: #1d4f8f;
    --blue-top: #2b86c5;
    --blue-bottom: #163f72;
    --white: #ffffff;
  }
  * { margin: 0; padding: 0; box-sizing: border-box; }
  html, body { width: 1200px; height: 1200px; overflow: hidden; background: var(--canvas); }
  .sign {
    position: absolute; left: 40px; top: 180px; width: 1120px; height: 840px;
    background: var(--sign); overflow: hidden;
    box-shadow: 0 6px 24px rgba(0,0,0,.12);
    font-family: 'Cinzel', serif;
  }
  .brand {
    position: absolute; top: 90px; left: 0; width: 100%;
    display: flex; align-items: center; justify-content: center; gap: 28px;
    color: var(--teal); font-weight: 400;
  }
  .brand-dot { width: 64px; height: 64px; border-radius: 50%; background: var(--teal); flex: none; }
  .brand-name { line-height: 1.05; text-align: right; }
  .brand-name .first { display: block; font-size: 76px; }
  .brand-name .rest { display: block; font-size: 38px; }
  .services {
    position: absolute; top: 400px; left: 0; width: 100%;
    display: flex; justify-content: space-around; padding: 0 60px;
  }
  .service { display: flex; flex-direction: column; align-items: center; width: 300px; }
  .service-icon {
    width: 140px; height: 140px; border-radius: 50%;
    background: var(--green); border: 5px solid var(--ring);
    display: flex; align-items: center; justify-content: center;
  }
  .service-icon svg { width: 78px; height: 78px; }
  .service-label {
    margin-top: 26px; font-size: 48px; font-weight: 900; color: var(--ink); letter-spacing: 1px;
  }
  .contact-band {
    position: absolute; left: 0; bottom: 0; width: 100%; height: 170px;
    background: linear-gradient(180deg, var(--blue-top), var(--blue-bottom));
  }
  .site-pill {
    position: absolute; left: 50%; top: 640px; transform: translateX(-50%);
    width: 560px; height: 78px; border-radius: 39px;
    background: linear-gradient(180deg, var(--green), var(--green-deep));
    display: flex; align-items: center; justify-content: center;
    color: var(--white); font-size: 34px; font-weight: 700; letter-spacing: 1px;
  }
  .phone {
    position: absolute; left: 0; bottom: 34px; width: 100%; text-align: center;
    color: var(--white); font-size: 82px; font-weight: 900; letter-spacing: 2px;
  }
</style>
</head>
<body>
  <main class="sign">
    <header class="brand">
      <span class="brand-dot"></span>
      <h1 class="brand-name" style="font-weight:400">
        <span class="first">Harlow</span>
        <span class="rest">Restoration</span>
        <span class="rest">Remodeling Group LLC</span>
      </h1>
    </header>

    <section class="services">
      <div class="service">
        <div class="service-icon">
          <svg viewBox="0 0 80 80" fill="none" stroke="#fff" stroke-width="5" stroke-linejoin="round">
            <path d="M8 40 L40 12 L72 40"/>
            <path d="M18 34 V70 H62 V34"/>
            <path d="M33 70 V50 H47 V70"/>
          </svg>
        </div>
        <span class="service-label">Roofing</span>
      </div>
      <div class="service">
        <div class="service-icon">
          <svg viewBox="0 0 80 80" fill="none" stroke="#fff" stroke-width="5" stroke-linejoin="round">
            <rect x="10" y="10" width="60" height="60"/>
            <path d="M40 10 V70 M10 40 H70"/>
          </svg>
        </div>
        <span class="service-label">Windows</span>
      </div>
      <div class="service">
        <div class="service-icon">
          <svg viewBox="0 0 80 80" fill="none" stroke="#fff" stroke-width="5" stroke-linejoin="round">
            <path d="M8 24 H72 L66 40 H14 Z"/>
            <path d="M34 40 V70 H46 V40"/>
          </svg>
        </div>
        <span class="service-label">Gutters</span>
      </div>
    </section>

    <footer class="contact-band">
      <p class="phone">CALL US: (555) 014-2290</p>
    </footer>
    <div class="site-pill">WWW.HARLOWLLC.COM</div>
  </main>
</body>
</html>
```